詳細はzipファイルにまとめておりおますので、こちらからダウンロードしてください。

http://3.hakobuya.nu/0522-k83920fa17de462093b8e1c7f06a35d9

【デザインの参考サイト】
クライアント様からは、以下の参考サイトを挙げていただいております。
http://plumtivra.com/
https://sorvik4417.com/

ただし、上記サイトはおしゃれではあるものの、少しアピールが弱いようにも思います。
最終的な成果(査定依頼や、来店予約)に結びつきやすいような工夫があれば嬉しいです。

【継続発注について】
まずはトップページのみのデザインをお願い致します。
トップページのデザインが決まりましたら、下層ページのデザインもお願いする予定です。(1ページ1~2万円程度の予定)
下層ページは2~3ページほどの予定ですので、総額12万円ぐらいの予定です。

【スマホ対応について】
コーディング時に、レスポンシブ対応する予定ですので、スマホ対応しやすいデザインにしていただければ助かります。

【レイアウトの変更などについて】
基本的にはワイヤーに沿って作っていただければと思います。
ただし、「もっとこうしたほうが良いのでは?」「こんな形はどうか?」といったようなご提案があれば、別途ご相談ください。

必要な資料は上記のzipファイルの中に入れておりますので、そちらをご覧ください。
もし不明な点があれば遠慮なくご連絡くださいませ。
1ページ
シンプル 複雑
単色 カラフル
暗い 明るい
日常 高級
遊び心 厳粛
未来的 伝統的
女性的 男性的
黄・オレンジ系
• 高解像度JPG (.jpg)
• イラストレーター形式 (.ai)
納品は、IllustratorでもPhotoshopでもFireworksでも、どのファイルでもOKです。

また、納品の際には使っているフォントをお教えください。
(使用フォントはモリサワ、もしくはフリーフォントでお願いします)
たくさんのご応募ありがとうございました。
非常に悩んだのですが、お一人の方を選ばせていただきました。
選に漏れた方々につきましては、お手数おかけしたにも関わらず何もお返しできずに心苦しくもあるのですが、ご了承いただければ幸いです。
またこれに懲りず、今後ともよろしくお願いいたします。
ありがとうございました!

いいデザインをしていただいた方が数人おられて、非常に悩みました。
その中で一番こちらの意図を汲み取っていただき、バランスの取れたデザインをしていただいた、ということで、こちらの方にお願いすることにしました。

たくさんのご応募ありがとうございました。
ありがとうございました!

```html
<!DOCTYPE html>
<html lang="ja">
<head>
<meta charset="utf-8">
<title>タカミエ | 高層階マンション買取サービス</title>
<link rel="stylesheet" href="https://fonts.googleapis.com/css2?family=Noto+Sans+JP:wght@400;500;700&family=Noto+Serif+JP:wght@500;700&display=swap">
<style>
:root{
  --orange:#f39800;
  --orange-dark:#d97f00;
  --orange-pale:#fdebc8;
  --ink:#333333;
  --muted:#777777;
  --line:#d9d9d9;
  --beige:#efe7dc;
  --grey-band:#eeeeee;
  --white:#ffffff;
  --dark:#2b2b2b;
}
*{margin:0;padding:0;box-sizing:border-box}
html,body{width:1200px;height:4884px;overflow:hidden}
body{font-family:"Noto Sans JP",sans-serif;color:var(--ink);background:var(--white);font-size:14px;line-height:1.7}
.serif{font-family:"Noto Serif JP",serif}
section,header,footer{position:relative;width:1200px;overflow:hidden}
.brand{font-family:"Noto Sans JP",sans-serif;font-weight:700;color:var(--ink);letter-spacing:.08em}

/* header */
.site-header{height:80px;display:flex;align-items:center;padding:0 160px;justify-content:space-between}
.site-header .brand{font-size:28px}
.brand-wrap{display:flex;align-items:center;gap:16px}
.brand-tag{font-size:11px;color:var(--muted);line-height:1.4}
.global-nav{display:flex;gap:26px;font-size:12px}

/* hero */
.hero{height:560px;background:linear-gradient(180deg,#9cc3e4 0%,#cfe0ec 38%,#a9b9c2 55%,#6f8f5e 78%,#3f6b32 100%)}
.hero-badge{position:absolute;left:480px;top:150px;width:240px;height:240px;background:rgba(255,255,255,.94);clip-path:polygon(50% 0,100% 25%,100% 75%,50% 100%,0 75%,0 25%);display:flex;flex-direction:column;align-items:center;justify-content:center;text-align:center}
.hero-badge p{font-size:13px;line-height:1.6}
.hero-badge .brand{font-size:36px;margin-top:8px}
.hero-dots{position:absolute;left:0;right:0;bottom:-30px}

.slider-dots{height:30px;display:flex;justify-content:center;gap:10px;align-items:center}
.slider-dots span{width:8px;height:8px;border-radius:50%;background:var(--line)}
.slider-dots span.on{background:var(--orange)}

.intro{height:100px;text-align:center;font-size:13px;line-height:1.9;padding-top:6px}

/* features */
.features{height:700px;background:var(--beige);padding-top:80px}
.feature-list{display:flex;justify-content:center;gap:20px}
.feature-card{width:280px;text-align:center}
.feature-photo{height:170px;background:linear-gradient(135deg,#d8d8d8,#b8b2aa)}
.feature-label{width:220px;margin:-36px auto 0;position:relative;background:var(--orange);color:var(--white);font-weight:700;font-size:15px;line-height:1.5;padding:12px 8px}
.feature-card p{font-size:13px;margin-top:22px;line-height:1.9}
.btn{display:flex;align-items:center;justify-content:center;background:var(--orange);color:var(--white);font-weight:700;position:relative}
.btn::after{content:"";position:absolute;right:22px;top:50%;margin-top:-5px;border-left:7px solid var(--white);border-top:5px solid transparent;border-bottom:5px solid transparent}
.features .btn{width:340px;height:62px;margin:70px auto 0;font-size:15px;line-height:1.4;text-align:center}

/* compare */
.compare{height:740px;padding-top:80px}
.section-title{text-align:center;font-size:24px;font-weight:700}
.compare-cols{display:flex;gap:40px;justify-content:center;margin-top:48px}
.compare-box{width:432px;height:540px;border:2px solid var(--line);padding:0 30px 30px}
.compare-box.ours{border-color:var(--orange);width:416px}
.compare-head{margin:0 -30px;height:46px;display:flex;align-items:center;justify-content:center;font-size:15px;font-weight:700;border-bottom:1px solid var(--line)}
.ours .compare-head{border-color:var(--orange-pale)}
.ours .brand-box{height:230px;display:flex;flex-direction:column;align-items:center;justify-content:center}
.ours .brand-box .brand{font-size:44px}
.diagram{height:230px;margin-top:10px;background:linear-gradient(180deg,#f3f3f3,#e4e4e4)}
.person{width:80px;height:70px;margin:10px auto 20px;background:#e6e6e6}
.check-list{list-style:none}
.check-list li{display:flex;gap:10px;font-size:12px;line-height:1.8;margin-bottom:14px}
.check-list svg{flex:0 0 16px;margin-top:4px}

/* faq */
.faq{height:770px}
.faq-photo{position:absolute;right:0;top:10px;width:260px;height:470px;background:linear-gradient(180deg,#f4f1ee,#e3d9d1)}
.faq .section-title{position:absolute;top:200px;left:0;right:0}
.faq-grid{position:absolute;top:270px;left:160px;width:880px;display:grid;grid-template-columns:repeat(3,280px);gap:20px}
.faq-card{border:1px solid var(--line);height:220px;background:var(--white)}
.faq-q{display:flex;align-items:stretch;border-bottom:1px solid var(--line)}
.faq-q b{width:40px;background:var(--ink);color:var(--white);display:flex;align-items:center;justify-content:center;font-size:20px}
.faq-q span{padding:8px 12px;font-size:12px;font-weight:700;line-height:1.6}
.faq-a{padding:14px 16px;color:var(--orange);font-size:12px;line-height:1.9}

.band{height:40px;background:var(--grey-band)}

/* results */
.results{height:1100px;padding-top:70px}
.results-list{margin-top:60px}
.result{display:flex;gap:20px;margin:0 160px 40px;height:250px}
.result-photo{width:240px;height:250px;background:linear-gradient(180deg,#a9cdea,#dfe6ea 45%,#b9b4ab)}
.result-body{width:330px}
.result-body h3{font-size:16px;line-height:1.5;margin-bottom:12px}
.spec{width:100%;border-collapse:collapse;font-size:12px}
.spec td{border-bottom:1px solid var(--line);padding:6px 4px}
.spec td:first-child{width:100px;font-weight:700}
.spec td:first-child::before{content:"";display:inline-block;width:10px;height:10px;background:var(--orange);margin-right:8px}
.result-note{width:270px;font-size:12px;line-height:1.9}
.result-note .btn{width:160px;height:40px;font-size:13px;margin-top:24px}
.results .more{width:300px;height:60px;margin:30px auto 0;font-size:15px}

/* cta */
.cta{height:280px;background:linear-gradient(135deg,#5b5550,#8a8178 60%,#6a625c);display:flex;justify-content:center;align-items:center;gap:40px}
.cta .btn{width:340px;height:84px;font-size:20px;box-shadow:0 4px 0 var(--orange-dark)}
.cta .btn small{font-size:13px;margin-left:4px}

/* footer */
.site-footer{height:450px;padding:70px 160px 0;display:flex;gap:40px}
.footer-info{width:270px;font-size:11px;line-height:1.9}
.footer-info .brand{font-size:26px;display:block;margin-bottom:16px}
.footer-nav{display:grid;grid-template-columns:repeat(3,110px);gap:6px 10px;font-size:11px;height:100px;margin-top:10px}
.footer-text{width:200px;font-size:11px;line-height:1.9}
.footer-photo{width:180px;height:240px;background:linear-gradient(180deg,#c5d7e6,#b5b0a8)}
.copyright{height:64px;background:var(--white);border-top:1px solid var(--line);text-align:center;font-size:11px;line-height:64px;color:var(--muted)}
</style>
</head>
<body>

<header class="site-header">
  <div class="brand-wrap">
    <span class="brand">タカミエ</span>
    <span class="brand-tag">7階以上の高層階限定<br>マンション買取サービス</span>
  </div>
  <nav class="global-nav">
    <span>サービスとは</span><span>買取について</span><span>買取実績</span><span>会社案内</span><span>お問い合わせ</span>
  </nav>
</header>

<section class="hero" role="img" aria-label="海と高層マンションが並ぶ街並みの写真">
  <div class="hero-badge">
    <p>7階以上の高層階の部屋、<br>買い取ります。</p>
    <span class="brand">タカミエ</span>
  </div>
</section>

<div class="slider-dots"><span class="on"></span><span></span><span></span><span></span><span></span><span></span></div>

<section class="intro">
  <p>「タカミエ」は、7階以上の高層階限定のマンション売却サービスです。</p>
  <p>高層階の眺望や日当たりの価値をきちんと評価し、仲介を通さず当社が直接お部屋を買い取ります。</p>
  <p>「タカミエ」だけのスピード査定で、住み替えやご売却を安心してお任せいただけます。</p>
</section>

<section class="features">
  <div class="feature-list">
    <div class="feature-card">
      <div class="feature-photo" role="img" aria-label="電卓と書類の写真"></div>
      <div class="feature-label">高層階の価値を<br>正当に評価します</div>
      <p>高層階マンションに特化しているので、<br>眺望や立地の価値を見逃さず<br>相場に見合った金額をご提示します。</p>
    </div>
    <div class="feature-card">
      <div class="feature-photo" role="img" aria-label="契約書にサインする手元の写真"></div>
      <div class="feature-label">仲介を通さず<br>直接買い取ります</div>
      <p>ご売却いただく方が<br>すぐに現金化できます。<br>手続きもスムーズに進みます。</p>
    </div>
    <div class="feature-card">
      <div class="feature-photo" role="img" aria-label="打ち合わせをする人の手元の写真"></div>
      <div class="feature-label">査定は無料で<br>お気軽にどうぞ</div>
      <p>もちろん査定は無料です。<br>強引な営業は一切ありませんので、<br>まずはお気軽にご相談ください。</p>
    </div>
  </div>
  <div class="btn">タカミエについて<br>詳しくはこちら</div>
</section>

<section class="compare">
  <h2 class="section-title serif">タカミエと一括見積りサイトとの違い</h2>
  <div class="compare-cols">
    <div class="compare-box">
      <div class="compare-head">一括見積りサイト</div>
      <div class="diagram" role="img" aria-label="一括見積りサイトから複数の不動産会社へ依頼が流れる図"></div>
      <div class="person" role="img" aria-label="お客様のアイコン"></div>
      <ul class="check-list">
        <li><svg width="16" height="16" viewBox="0 0 16 16"><rect width="16" height="16" fill="#333"/><path d="M3 8l3 3 7-7" stroke="#fff" stroke-width="2" fill="none"/></svg><span>多くの業者から一度に連絡が来るため、対応に追われてしまいます。査定額の比較にも手間がかかります。</span></li>
        <li><svg width="16" height="16" viewBox="0 0 16 16"><rect width="16" height="16" fill="#333"/><path d="M3 8l3 3 7-7" stroke="#fff" stroke-width="2" fill="none"/></svg><span>仲介業者が間に入るため、手数料がかかり売却までの期間も長くなりがちです。</span></li>
      </ul>
    </div>
    <div class="compare-box ours">
      <div class="compare-head">タカミエ</div>
      <div class="brand-box"><span class="brand">タカミエ</span></div>
      <div class="person" role="img" aria-label="お客様のアイコン"></div>
      <ul class="check-list">
        <li><svg width="16" height="16" viewBox="0 0 16 16"><rect width="16" height="16" fill="#f39800"/><path d="M3 8l3 3 7-7" stroke="#fff" stroke-width="2" fill="none"/></svg><span>窓口がひとつなので、ご連絡は当社からのみ。高層階の価値を踏まえた査定額をすぐにご提示します。</span></li>
        <li><svg width="16" height="16" viewBox="0 0 16 16"><rect width="16" height="16" fill="#f39800"/><path d="M3 8l3 3 7-7" stroke="#fff" stroke-width="2" fill="none"/></svg><span>当社が直接買い取るので、仲介手数料は不要です。ご希望の時期に合わせて売却できます。</span></li>
      </ul>
    </div>
  </div>
</section>

<section class="faq">
  <div class="faq-photo" role="img" aria-label="考えごとをする女性の写真"></div>
  <h2 class="section-title serif">よくある質問</h2>
  <div class="faq-grid">
    <div class="faq-card"><div class="faq-q"><b>Q</b><span>査定にはどのくらいの時間がかかりますか？</span></div><p class="faq-a">お問い合わせから最短で当日中に概算の査定額をお伝えします。現地確認後、正式な金額をご提示いたします。</p></div>
    <div class="faq-card"><div class="faq-q"><b>Q</b><span>住宅ローンが残っていても売却できますか？</span></div><p class="faq-a">はい、売却が可能です。売却代金でローンを完済する流れをご案内しますのでご安心ください。</p></div>
    <div class="faq-card"><div class="faq-q"><b>Q</b><span>7階未満のお部屋は対象外ですか？</span></div><p class="faq-a">当サービスは7階以上の高層階限定です。それ以外の物件は提携会社をご紹介いたします。</p></div>
    <div class="faq-card"><div class="faq-q"><b>Q</b><span>住んだままでも査定を受けられますか？</span></div><p class="faq-a">もちろん可能です。ご入居中のままでも、ご都合の良い日時に訪問いたします。</p></div>
    <div class="faq-card"><div class="faq-q"><b>Q</b><span>売却の費用はどのくらいかかりますか？</span></div><p class="faq-a">当社が直接買い取るため、仲介手数料はかかりません。登記費用などの詳細は個別にご説明します。</p></div>
    <div class="faq-card"><div class="faq-q"><b>Q</b><span>査定後に売却を断ることはできますか？</span></div><p class="faq-a">はい、査定額にご納得いただけない場合はお断りいただいて構いません。費用は一切かかりません。</p></div>
  </div>
</section>

<div class="band"></div>

<section class="results">
  <h2 class="section-title serif">買取実績</h2>
  <div class="results-list">
    <article class="result">
      <div class="result-photo" role="img" aria-label="白い高層マンションの外観写真"></div>
      <div class="result-body">
        <h3>湾岸エリア 高層タワーマンション 眺望良好の角部屋</h3>
        <table class="spec">
          <tr><td>階</td><td>12階</td></tr>
          <tr><td>間取タイプ</td><td>3LDK</td></tr>
          <tr><td>買取価格</td><td>3,500万円</td></tr>
          <tr><td>地域</td><td>湾岸エリア</td></tr>
        </table>
      </div>
      <div class="result-note">
        <p>眺望の良さを評価し、周辺相場を上回る価格で買い取りました。お問い合わせから約2週間で決済まで完了しました。</p>
        <div class="btn">詳しくみる</div>
      </div>
    </article>
    <article class="result">
      <div class="result-photo" role="img" aria-label="ベージュの高層マンションの外観写真"></div>
      <div class="result-body">
        <h3>駅近エリア 築浅マンション 南向きの明るいお部屋</h3>
        <table class="spec">
          <tr><td>階</td><td>10階</td></tr>
          <tr><td>間取タイプ</td><td>2LDK</td></tr>
          <tr><td>買取価格</td><td>2,800万円</td></tr>
          <tr><td>地域</td><td>駅前エリア</td></tr>
        </table>
      </div>
      <div class="result-note">
        <p>住み替えのご予定に合わせ、引き渡し時期を調整して買い取りました。ローン残債の手続きもサポートしました。</p>
        <div class="btn">詳しくみる</div>
      </div>
    </article>
    <article class="result">
      <div class="result-photo" role="img" aria-label="グレーの大型マンションの外観写真"></div>
      <div class="result-body">
        <h3>山手エリア 大規模マンション 夜景が望める上層階</h3>
        <table class="spec">
          <tr><td>階</td><td>15階</td></tr>
          <tr><td>間取タイプ</td><td>4LDK</td></tr>
          <tr><td>買取価格</td><td>4,200万円</td></tr>
          <tr><td>地域</td><td>山手エリア</td></tr>
        </table>
      </div>
      <div class="result-note">
        <p>相続されたお部屋を、ご家族のご意向に沿って現況のまま買い取りました。室内の片付けも当社で対応しました。</p>
        <div class="btn">詳しくみる</div>
      </div>
    </article>
  </div>
  <div class="btn more">買取実績をもっとみる</div>
</section>

<section class="cta" role="img" aria-label="明るい室内の写真を背景にした申込み案内">
  <div class="btn">買取無料査定<small>はこちら</small></div>
  <div class="btn">ご来店予約<small>はこちら</small></div>
</section>

<footer class="site-footer">
  <div class="footer-info">
    <span class="brand">タカミエ</span>
    <p>運営：サンプルエステート株式会社</p>
    <p>〒000-0000 架空県中央市みなと町1-2-3</p>
    <p>サンプルビル5階</p>
    <p>TEL 000-000-0000</p>
  </div>
  <div>
    <div class="footer-nav">
      <span>サービスとは</span><span>買取の流れ</span><span>会社案内</span>
      <span>買取について</span><span>よくある質問</span><span>個人情報保護</span>
      <span>買取実績</span><span>お問い合わせ</span><span>サイトマップ</span>
    </div>
  </div>
  <div class="footer-text">
    <p>「タカミエ」は、7階以上の高層階マンションを専門に買い取るサービスです。眺望や立地の価値を正しく評価し、安心のお取引をお約束します。</p>
  </div>
  <div class="footer-photo" role="img" aria-label="高層マンションの外観写真"></div>
</footer>

<div class="copyright">Copyright © 2017 Sample Estate Co., Ltd. All Rights Reserved.</div>

</body>
</html>
```